Staff Falcons WIX Design Project - website for HR Professional Community

Redesign of website to incorporate new logo - we are looking for a web design partner - will include adhoc work going forward.

Current website - www.thestafffalcons.co.uk

The 'Onward to Radiant' content is not required on the new site.

Target Market(s)

HR professionals

Industry/Entity Type

Professional Network

Coding

Coded - Design and coding required

Requirements
Must have
• A partners page
Nice to have
• an events page

```html
<!DOCTYPE html>
<html lang="en">
<head>
<meta charset="utf-8">
<title>Staff Falcons – The UK's Most Vibrant Online Community for HR Professionals</title>
<link rel="stylesheet" href="https://fonts.googleapis.com/css2?family=Barlow:wght@400;500;600;700&family=Roboto+Condensed:wght@300;400;700&display=swap">
<style>
:root{
  --orange:#f28c1c;
  --orange-soft:#f7b26a;
  --ink:#1f1f1f;
  --text:#333333;
  --muted:#666666;
  --card:#f2f2f2;
  --panel:#ececec;
  --white:#ffffff;
  --footer:#232323;
  --line:#dddddd;
}
*{box-sizing:border-box;margin:0;padding:0}
html,body{width:1200px;height:5208px;overflow:hidden}
body{position:relative;background:var(--white);font-family:"Roboto Condensed",Arial,sans-serif;color:var(--text)}
.abs{position:absolute}
.heading{font-family:"Barlow",Arial,sans-serif;font-weight:700;color:var(--ink);text-transform:uppercase}
.accent{color:var(--orange)}
.dots{position:absolute;height:0;border-top:2px dotted var(--orange);width:80px}
.pill{position:absolute;display:flex;align-items:center;justify-content:center;border-radius:20px;font-family:"Barlow",Arial,sans-serif;font-weight:600;font-size:14px;white-space:nowrap}
.pill--solid{background:var(--orange);color:var(--white)}
.pill--white{background:var(--white);color:var(--orange)}
.pill--outline{border:2px solid var(--orange);color:var(--orange);background:var(--white)}
.pill--dark{border:2px solid var(--ink);color:var(--ink);background:var(--white)}
.social{position:absolute;width:36px;height:36px;border:2px solid var(--orange);border-radius:50%}

/* header */
.site-header{position:absolute;left:0;top:0;width:1200px;height:130px;background:var(--white)}
.brand{position:absolute;font-family:"Barlow",Arial,sans-serif;font-weight:600;color:var(--orange);letter-spacing:1px}
.brand-dot{position:absolute;width:34px;height:34px;border-radius:50%;background:var(--orange)}
.nav{position:absolute;right:174px;top:82px;display:flex;font-family:"Barlow",Arial,sans-serif;font-weight:600;font-size:13px;color:var(--ink);text-transform:uppercase;white-space:nowrap}
.nav span{padding:0 11px;border-left:1px solid #bbb;line-height:14px}
.nav span:first-child{border-left:none;color:var(--orange)}
.nav span:last-child{padding-right:0}
.signup{position:absolute;left:832px;top:18px;width:194px;height:40px;border:2px solid var(--orange);display:flex;align-items:center;justify-content:center;font-family:"Barlow",Arial,sans-serif;font-weight:600;font-size:13px;color:var(--ink)}

/* hero */
.hero{position:absolute;left:0;top:130px;width:1200px;height:628px;background:linear-gradient(100deg,#2d2b2a 0%,#5b4a3e 40%,#9a8a7c 70%,#cfc7be 100%)}
.hero-title{position:absolute;left:170px;top:150px;font-family:"Barlow",Arial,sans-serif;font-weight:700;font-size:54px;line-height:70px;color:var(--white);text-transform:uppercase;letter-spacing:1px}
.hero-sub{position:absolute;left:170px;top:296px;font-family:"Roboto Condensed",Arial,sans-serif;font-weight:300;font-size:38px;line-height:46px;color:var(--white)}

/* service cards */
.service{position:absolute;top:845px;width:272px;height:385px;background:var(--card);padding:52px 28px 0}
.service--featured{background:var(--orange);color:var(--white)}
.service h3{font-family:"Barlow",Arial,sans-serif;font-weight:700;font-size:28px;color:var(--ink);text-transform:uppercase}
.service--featured h3{color:var(--white)}
.service .dots{left:28px;top:100px}
.service--featured .dots{border-color:var(--white)}
.service p{position:absolute;left:28px;right:22px;top:120px;font-size:14px;line-height:22px;color:var(--text)}
.service--featured p{color:var(--white);font-weight:700}
.service p b{font-weight:700}

/* why */
.why-photo{position:absolute;left:170px;top:1322px;width:408px;height:518px;background:linear-gradient(180deg,#2f5a4e 0%,#3d6b5c 55%,#d48a9a 80%,#c97a8c 100%)}
.why-list{position:absolute;left:620px;top:1570px;width:410px}
.why-list li{list-style:none;height:45px;border-bottom:1px solid var(--line);display:flex;align-items:center;font-family:"Barlow",Arial,sans-serif;font-weight:600;font-size:14px;color:var(--ink);text-transform:uppercase}
.why-list li:last-child{border-bottom:none}
.why-list svg{margin-right:14px}

/* job board */
.question{position:absolute;left:170px;display:flex;font-family:"Barlow",Arial,sans-serif;font-weight:500;font-size:14px;line-height:20px;color:var(--ink);text-transform:uppercase}
.question i{font-style:normal;flex:0 0 24px;height:24px;background:#fde8d2;color:var(--orange);font-weight:700;display:flex;align-items:center;justify-content:center;margin-right:20px;margin-top:-2px}
.jobs-box{position:absolute;left:170px;top:2186px;width:408px;height:182px;border:1px solid var(--line);padding:18px 28px}
.jobs-box p{font-family:"Barlow",Arial,sans-serif;font-weight:700;font-size:28px;line-height:37px;color:var(--orange);text-transform:uppercase}

/* team */
.member{position:absolute;top:2762px;width:272px;height:386px;background:var(--card)}
.member-photo{position:absolute;left:0;top:0;width:272px;height:270px}
.member-info{position:absolute;left:0;top:270px;width:272px;height:116px;text-align:center;padding-top:28px}
.member--lead .member-info{background:var(--orange);color:var(--white)}
.member h4{font-family:"Barlow",Arial,sans-serif;font-weight:700;font-size:26px;text-transform:uppercase;color:var(--ink)}
.member--lead h4{color:var(--white)}
.member small{display:block;margin-top:6px;font-family:"Barlow",Arial,sans-serif;font-weight:500;font-size:13px;letter-spacing:1px;text-transform:uppercase;color:var(--text)}
.member--lead small{color:var(--white)}

/* testimonial */
.testimonial{position:absolute;left:0;top:3242px;width:1200px;height:520px;background:linear-gradient(120deg,#1d2023 0%,#30343a 45%,#43403d 80%,#2a2624 100%)}
.testimonial .rule{position:absolute;left:170px;width:856px;border-top:2px dotted rgba(242,140,28,.6)}
.quote-mark{position:absolute;font-family:"Barlow",Arial,sans-serif;font-weight:700;font-size:90px;line-height:90px;color:var(--orange)}

/* blogs */
.blog{position:absolute;top:3955px;width:272px;height:385px;background:var(--card);text-align:center}
.blog-image{position:absolute;left:16px;top:17px;width:240px;height:238px}
.blog-date{position:absolute;left:96px;top:286px;width:80px;height:22px;border-radius:11px;background:var(--white);font-size:12px;line-height:22px;color:var(--text)}
.blog h5{position:absolute;left:20px;right:20px;top:320px;font-family:"Roboto Condensed",Arial,sans-serif;font-weight:700;font-size:17px;line-height:24px;color:var(--ink)}

/* newsletter */
.news-photo{position:absolute;left:0;top:4458px;width:464px;height:432px;background:linear-gradient(135deg,#e7d8e6 0%,#b58db0 35%,#a3715c 65%,#4a4a55 100%)}
.news-panel{position:absolute;left:464px;top:4458px;width:736px;height:432px;background:var(--panel)}
.news-panel h2{position:absolute;left:0;width:736px;top:70px;text-align:center;font-family:"Barlow",Arial,sans-serif;font-weight:600;font-size:30px;line-height:38px;color:var(--ink)}
.field{position:absolute;width:258px;height:38px;border:2px solid var(--orange);border-radius:20px;display:flex;align-items:center;justify-content:center;font-family:"Barlow",Arial,sans-serif;font-weight:600;font-size:14px;color:var(--ink)}

/* footer */
.site-footer{position:absolute;left:0;top:4890px;width:1200px;height:318px;background:var(--footer);color:var(--white)}
.contact{position:absolute;left:172px;display:flex;align-items:center;font-size:14px;line-height:18px}
.contact .ico{width:36px;height:36px;border:2px solid var(--orange);border-radius:50%;display:flex;align-items:center;justify-content:center;margin-right:18px;flex:0 0 36px}
</style>
</head>
<body>

<header class="site-header">
  <div class="brand-dot" style="left:228px;top:22px"></div>
  <div class="brand" style="left:170px;top:76px;font-size:28px">STAFF FALCONS</div>
  <div class="social" style="left:652px;top:20px" aria-label="Social profile"></div>
  <div class="social" style="left:706px;top:20px" aria-label="Social profile"></div>
  <div class="social" style="left:760px;top:20px" aria-label="Video channel"></div>
  <div class="signup">NEWSLETTER SIGNUP</div>
  <nav class="nav">
    <span>Home</span><span>Our Story</span><span>Services</span><span>Board</span><span>Coaching</span><span>Partners</span><span>Blog</span><span>Contacts</span>
  </nav>
</header>

<section class="hero" role="img" aria-label="Two professionals high-fiving across an office desk">
  <h1 class="hero-title">Welcome to the<br><span class="accent">Staff Falcons</span>!</h1>
  <p class="hero-sub">The UK's Most Vibrant Online<br>Community for HR Professionals.</p>
  <div class="pill pill--solid" style="left:170px;top:432px;width:300px;height:36px">SIGN UP FOR OUR NEWSLETTER</div>
</section>

<section class="services">
  <article class="service service--featured" style="left:170px">
    <h3>Community</h3><div class="dots"></div>
    <p>Our Huddle Community Group enables you to connect with a fast-growing, highly engaged community of over 17k HR professionals</p>
    <div class="pill pill--white" style="left:28px;top:311px;width:216px;height:36px">Join our Huddle Group</div>
  </article>
  <article class="service" style="left:464px">
    <h3>Jobs</h3><div class="dots"></div>
    <p>Get your HR job in front of <b>17k HR Professionals</b><br><b>FREE</b> job postings for members of our Huddle group<br><br>Open to non-members<br><b>ONLY £100+vat</b></p>
    <div class="pill pill--solid" style="left:28px;top:311px;width:216px;height:36px">View Our Jobs Board</div>
  </article>
  <article class="service" style="left:756px">
    <h3>Coaching</h3><div class="dots"></div>
    <p>Our coaching club is currently over subscribed and we are not currently accepting requests for support.<br><br><b>Doors are open now for registrations!</b></p>
    <div class="pill pill--solid" style="left:28px;top:311px;width:216px;height:36px">Join Our Coaching Club</div>
  </article>
</section>

<section class="why">
  <div class="why-photo" role="img" aria-label="Founder in a pink jumper writing at a laptop"></div>
  <h2 class="heading abs" style="left:620px;top:1326px;font-size:40px">Why <span class="accent">Staff Falcons</span>?</h2>
  <div class="dots" style="left:620px;top:1398px"></div>
  <p class="abs" style="left:620px;top:1426px;width:380px;font-size:14px;line-height:22px">I had a gut feeling that we might be onto something so we started small, with just 30 members.</p>
  <p class="abs" style="left:620px;top:1492px;width:380px;font-size:14px;line-height:22px">Fast forward almost four years and we have evolved The Staff Falcons into a thriving community</p>
  <ul class="why-list">
    <li><svg width="18" height="18" viewBox="0 0 18 18"><rect x="1" y="3" width="13" height="13" fill="none" stroke="#1f1f1f" stroke-width="1.5"/><path d="M4 9l3 3 9-10" fill="none" stroke="#1f1f1f" stroke-width="1.5"/></svg><span class="accent">17</span>K HR Professionals</li>
    <li><svg width="18" height="18" viewBox="0 0 18 18"><rect x="1" y="3" width="13" height="13" fill="none" stroke="#1f1f1f" stroke-width="1.5"/><path d="M4 9l3 3 9-10" fill="none" stroke="#1f1f1f" stroke-width="1.5"/></svg><span class="accent">100</span>&nbsp;New members each and every week!</li>
    <li><svg width="18" height="18" viewBox="0 0 18 18"><rect x="1" y="3" width="13" height="13" fill="none" stroke="#1f1f1f" stroke-width="1.5"/><path d="M4 9l3 3 9-10" fill="none" stroke="#1f1f1f" stroke-width="1.5"/></svg>Give more than you take</li>
    <li><svg width="18" height="18" viewBox="0 0 18 18"><rect x="1" y="3" width="13" height="13" fill="none" stroke="#1f1f1f" stroke-width="1.5"/><path d="M4 9l3 3 9-10" fill="none" stroke="#1f1f1f" stroke-width="1.5"/></svg>Collaboration and connection</li>
  </ul>
  <div class="pill pill--outline" style="left:620px;top:1788px;width:124px;height:38px">Our Story</div>
</section>

<section class="job-board">
  <h2 class="heading abs" style="left:0;width:1200px;top:1922px;text-align:center;font-size:40px">The <span class="accent">Staff Falcons</span> Job Board!</h2>
  <div class="dots" style="left:560px;top:1998px"></div>
  <div class="question" style="top:2054px;width:380px"><i>?</i><span>Are you looking to share your HR roles with our audience?</span></div>
  <div class="question" style="top:2120px;width:380px"><i>?</i><span>Are you an HR job seeker looking for your next adventure?</span></div>
  <div class="jobs-box"><p>We are fast becoming<br>the place to share and<br>seek for HR jobs<br>in the UK</p></div>
  <p class="abs" style="left:170px;top:2404px;width:380px;font-size:21px;line-height:30px;color:var(--ink)"><span class="accent">And get this!...</span> If you're a member of our <b class="accent">Huddle group</b> you can share your jobs for <span class="accent">FREE!</span></p>
  <div class="pill pill--dark" style="left:170px;top:2524px;width:128px;height:38px">View Jobs</div>
  <div class="abs" style="left:620px;top:2050px;width:406px;height:518px;background:linear-gradient(160deg,#3c4a52 0%,#7d6a58 45%,#c3243a 70%,#6b5a4a 100%)" role="img" aria-label="Wooden door with a red hiring sign and apply today plaque"></div>
</section>

<section class="team">
  <h2 class="heading abs" style="left:0;width:1200px;top:2648px;text-align:center;font-size:40px">Meet the <span class="accent">Team</span></h2>
  <div class="dots" style="left:560px;top:2724px"></div>
  <article class="member member--lead" style="left:170px">
    <div class="member-photo" style="background:linear-gradient(180deg,#d9d9d9,#8e8e8e)" role="img" aria-label="Portrait of the founder"></div>
    <div class="member-info"><h4>Maren Holt</h4><small>Founder The Staff Falcons</small></div>
  </article>
  <article class="member" style="left:464px">
    <div class="member-photo" style="background:linear-gradient(180deg,#ededed,#9a9a9a)" role="img" aria-label="Portrait of the head of partnerships"></div>
    <div class="member-info"><h4>Owen Pardy</h4><small>Head of Partnerships</small></div>
  </article>
  <article class="member" style="left:756px">
    <div class="member-photo" style="background:linear-gradient(180deg,#c9c9c9,#6f6f6f)" role="img" aria-label="Portrait of the creative editor"></div>
    <div class="member-info"><h4>Tess Pardy</h4><small>Creative Editor</small></div>
  </article>
</section>

<section class="testimonial" role="img" aria-label="Workshop room with attendees at laptops listening to a speaker">
  <div class="rule" style="top:126px"></div>
  <div class="rule" style="top:398px"></div>
  <div class="quote-mark" style="left:196px;top:168px">“</div>
  <p class="abs" style="left:268px;top:196px;width:680px;font-size:16px;line-height:26px;color:var(--white)">I love the Falcons group. It is a great place for like minded people to discuss their thoughts and ideas and to support each other. Also a great place for some light relief after a long week when reading the amusing stories and scenarios people in HR have to address.</p>
  <p class="abs heading" style="left:268px;top:302px;font-size:20px;color:var(--orange);font-weight:600">Nadia, HR Professional</p>
  <div class="quote-mark" style="left:954px;top:296px">”</div>
</section>

<section class="blogs">
  <h2 class="heading abs" style="left:0;width:1200px;top:3838px;text-align:center;font-size:40px">Our <span class="accent">Blogs</span></h2>
  <div class="dots" style="left:560px;top:3914px"></div>
  <article class="blog" style="left:170px">
    <div class="blog-image" style="background:linear-gradient(135deg,#bdbdbd,#8a8a8a)" role="img" aria-label="Blog cover with tips from the founder"></div>
    <div class="blog-date">Mar 21, 2022</div>
    <h5>It's not every day you come across a role like this one!</h5>
  </article>
  <article class="blog" style="left:464px">
    <div class="blog-image" style="background:linear-gradient(135deg,#9c9c9c,#5f5f5f)" role="img" aria-label="Blog cover announcing new HR jobs added"></div>
    <div class="blog-date">Mar 21, 2022</div>
    <h5>It's not every day you come across a role like this one!</h5>
  </article>
  <article class="blog" style="left:756px">
    <div class="blog-image" style="background:linear-gradient(135deg,#7a7a7a,#d6d6d6)" role="img" aria-label="Blog cover for a coming soon partner announcement"></div>
    <div class="blog-date">Mar 21, 2022</div>
    <h5>It's not every day you come across a role like this one!</h5>
  </article>
</section>

<section class="newsletter">
  <div class="news-photo" role="img" aria-label="Two community members smiling at a live event"></div>
  <div class="news-panel">
    <h2>Sign up to Receive Our <span class="accent">Bi-Weekly<br>Newsletter</span> Direct to Your Inbox</h2>
    <div class="field" style="left:30px;top:200px">Full Name</div>
    <div class="field" style="left:304px;top:200px">Email Address</div>
    <div class="field" style="left:30px;top:268px">Job Title</div>
    <div class="field" style="left:304px;top:268px">Company</div>
    <div class="pill pill--solid" style="left:228px;top:342px;width:140px;height:36px">Submit</div>
  </div>
</section>

<footer class="site-footer">
  <div class="contact" style="top:114px"><span class="ico"><svg width="14" height="18" viewBox="0 0 14 18"><path d="M7 1a6 6 0 0 0-6 6c0 4.5 6 10 6 10s6-5.5 6-10a6 6 0 0 0-6-6z" fill="none" stroke="#f28c1c" stroke-width="1.6"/><circle cx="7" cy="7" r="2" fill="#f28c1c"/></svg></span><span>14 – 16 Larkfield Street<br>London, E2 4QP</span></div>
  <div class="contact" style="top:174px"><span class="ico"><svg width="16" height="12" viewBox="0 0 16 12"><rect x="1" y="1" width="14" height="10" fill="none" stroke="#f28c1c" stroke-width="1.5"/><path d="M1 1l7 6 7-6" fill="none" stroke="#f28c1c" stroke-width="1.5"/></svg></span><span>hello@thestafffalcons.co.uk</span></div>
  <div class="brand-dot" style="left:583px;top:86px"></div>
  <div class="brand" style="left:0;width:1200px;text-align:center;top:136px;font-size:32px">STAFF FALCONS</div>
  <p class="abs" style="left:0;width:1200px;text-align:center;top:206px;font-size:14px">© 2022. thestafffalcons.co.uk</p>
  <div class="social" style="left:882px;top:136px" aria-label="Social profile"></div>
  <div class="social" style="left:936px;top:136px" aria-label="Social profile"></div>
  <div class="social" style="left:990px;top:136px" aria-label="Video channel"></div>
</footer>

</body>
</html>
```